Redesign Of Flower Delivery Subscription Service Website

I need a revamped website of www.petal-rush.com

Please revamp current design using same content....

Target Market(s)

people who buy flowers. Brides, wedding planners, wedding photographer, married man, boyfriend, etc.

Industry/Entity Type

Florist

Number of Pages Required

5+ page

Colors

Designer to choose colors to be used in the design.

Requirements
Must have
• I need a revamped website of www.petal-rush.com
• Please revamp current design using same content....
Nice to have
Should not have

```html
<!DOCTYPE html>
<html lang="en">
<head>
<meta charset="utf-8">
<title>Petal Rush – Monthly Flower Delivery</title>
<link href="https://fonts.googleapis.com/css2?family=Open+Sans:wght@400;600;700&display=swap" rel="stylesheet">
<style>
:root{
  --page-bg:#e2e9ec;
  --white:#ffffff;
  --green:#8fd14f;
  --green-soft:#a9dd76;
  --dark:#2f2c2b;
  --text:#4a4a4a;
  --muted:#666;
  --orange:#e6a023;
  --price:#f2a92c;
}
*{box-sizing:border-box;margin:0;padding:0}
html,body{width:1200px;height:1200px;overflow:hidden}
body{background:var(--page-bg);font-family:"Open Sans",sans-serif;color:var(--text);position:relative}
.page{position:absolute;left:54px;top:0;width:1092px;height:1200px;background:var(--white);overflow:hidden}
.abs{position:absolute}

.top-links{left:110px;top:12px;display:flex;gap:20px;font-size:12px;color:var(--muted)}
.top-rule{left:101px;top:36px;width:889px;height:1px;background:#e6e6e6}
.social{right:108px;top:12px;display:flex;gap:8px}
.social span{width:15px;height:15px;border-radius:50%;background:#3a3a3a;display:block}
.social span.active{background:var(--green)}

.brand{left:102px;top:48px;font-size:27px;font-weight:600;color:var(--dark);letter-spacing:1px}
.call{left:595px;top:47px;display:flex;align-items:center;gap:8px}
.call-label{font-size:11px;color:var(--muted);line-height:1.3}
.call-number{font-size:15px;color:var(--dark);letter-spacing:.5px}
.login{left:900px;top:58px;width:80px;height:23px;background:var(--green);color:#fff;font-size:12px;font-weight:600;text-align:center;line-height:23px}

.nav{left:0;top:97px;width:1092px;height:48px;background:linear-gradient(90deg,var(--green) 0%,#6f9a3f 35%,#4a4a35 60%,#2d2c2b 100%);display:flex}
.nav a{color:#fff;text-decoration:none;font-size:14.5px;font-weight:600;padding:0 14px;line-height:48px;border-right:1px solid rgba(0,0,0,.12)}
.nav a:first-child{padding-left:117px}
.nav a:last-child{border-right:none}

.hero{left:0;top:145px;width:1092px;height:436px;background:linear-gradient(100deg,#8c8079 0%,#a69a92 30%,#7b7670 50%,#c8bba8 70%,#e9dcc0 100%)}
.hero-box{left:101px;top:101px;width:464px;height:234px;background:rgba(55,52,50,.72);text-align:center;color:#fff}
.hero-title{margin-top:38px;font-size:38px;font-weight:700;letter-spacing:2px}
.hero-sub{margin-top:6px;font-size:16.5px;font-weight:600;letter-spacing:.8px}
.hero-price{margin-top:4px;font-size:16.5px;font-weight:600;letter-spacing:.8px}
.hero-price em{font-style:normal;color:var(--price)}
.buy{display:inline-block;margin-top:15px;width:160px;height:48px;line-height:48px;background:var(--green);font-size:16px;font-weight:700;letter-spacing:2px}

.card{top:629px;width:272px;height:285px}
.card-purple{left:101px;background:linear-gradient(160deg,#c9d4c8,#8a4f7c 45%,#6b2e55 70%,#5a3a2e)}
.card-text{left:409px;background:#343232;color:#fff;text-align:center}
.card-text h3{margin-top:56px;font-size:14.5px;font-weight:700;letter-spacing:2px}
.card-text hr{width:116px;margin:12px auto 14px;border:none;border-top:1px solid #fff}
.card-text p{font-size:11.5px;line-height:16px;letter-spacing:1px;padding:0 26px}
.card-pink{left:717px;background:radial-gradient(circle at 50% 40%,#e9967f 0%,#b0775e 35%,#f4f0ee 72%)}

.signup{left:0;top:962px;width:1092px;height:142px;background:linear-gradient(180deg,var(--green) 0%,var(--green) 55%,#f5f8f3 100%)}
.signup-text{left:140px;top:30px;color:#fff;font-size:19.5px;font-weight:600;letter-spacing:2.4px;line-height:24px}
.email{left:502px;top:31px;width:318px;height:48px;background:var(--green-soft);color:#e9f6dd;font-size:14.5px;letter-spacing:1.5px;line-height:48px;padding-left:23px}
.submit{left:820px;top:31px;width:160px;height:48px;background:var(--orange);color:#fff;font-size:14.5px;font-weight:700;letter-spacing:2.5px;text-align:center;line-height:48px}

.extras{left:0;top:1104px;width:1092px;height:96px;background:linear-gradient(90deg,#e4b9c7 0%,#f1e6ea 30%,#f6f7f5 60%)}
.extras-title{left:662px;top:20px;font-size:24px;font-weight:700;color:#3a3a3a;letter-spacing:1px;line-height:29px}
.extras-title em{font-style:normal;color:var(--green)}
</style>
</head>
<body>
<div class="page">
  <div class="abs top-links"><span>Blog</span><span>Corporate Arrangements</span><span>Help</span></div>
  <div class="abs social" aria-label="Social links"><span></span><span class="active"></span><span></span><span></span></div>
  <div class="abs top-rule"></div>

  <div class="abs brand">Petal Rush</div>
  <div class="abs call">
    <svg width="20" height="20" viewBox="0 0 24 24" aria-hidden="true"><path fill="#8fd14f" d="M6.6 10.8a15.1 15.1 0 0 0 6.6 6.6l2.2-2.2c.3-.3.7-.4 1-.2 1.1.4 2.3.6 3.6.6.6 0 1 .4 1 1V20c0 .6-.4 1-1 1A17 17 0 0 1 3 4c0-.6.4-1 1-1h3.5c.6 0 1 .4 1 1 0 1.3.2 2.5.6 3.6.1.3 0 .7-.2 1z"/></svg>
    <div><div class="call-label">Call us</div><div class="call-number">555-014-2290</div></div>
  </div>
  <div class="abs login">Login</div>

  <nav class="abs nav">
    <a>HOME</a><a>HOW IT WORKS</a><a>DELIVERY AREAS</a><a>FRANCHISE</a><a>FREE FLOWERS MONTHLY</a>
  </nav>

  <section class="abs hero" role="img" aria-label="Person with a phone and coffee cup beside a bouquet of cream roses wrapped in paper">
    <div class="abs hero-box">
      <div class="hero-title">ALWAYS FRESH</div>
      <div class="hero-sub">Beautiful Flower Arrangements Delivered Monthly</div>
      <div class="hero-price">NOW ONLY <em>$69.95/MTH</em> ($100 VALUE)</div>
      <div class="buy">BUY NOW</div>
    </div>
  </section>

  <div class="abs card card-purple" role="img" aria-label="Purple and lilac rose arrangement in a glass vase with a ribbon"></div>
  <div class="abs card card-text">
    <h3>BUT NEVER FORGET AGAIN</h3>
    <hr>
    <p>When setting up your account, you can choose exact delivery dates for the months that have special days such as your Anniversary, Birthday, Valentines Day and Mothers Day. You might forget but we won’t, we have got ya covered!</p>
  </div>
  <div class="abs card card-pink" role="img" aria-label="Pink rose bouquet in a red glass vase"></div>

  <section class="abs signup">
    <div class="abs signup-text">ENTER YOUR EMAIL TO<br>RECEIVE A FREE UPGRADE</div>
    <div class="abs email">Your email</div>
    <div class="abs submit">SUBMIT</div>
  </section>

  <section class="abs extras" role="img" aria-label="Soft pink and white flower petals">
    <div class="abs extras-title">With <em>Petal Rush</em> flowers<br>you also get:</div>
  </section>
</div>
</body>
</html>
```